Dog Walking logo design

Dog Walking, Dog Sitting, Pet Taxi, Doggy Day Care. I'm looking for a design that shows a man walking 3 dogs. The dogs are on leads and we only see the mans legs. I'm open to suggestion re: the image of a sole of a boot associated with walking. I would like my company name as part of or incorporated into any image or logo.

Industry/Entity Type

It Company

Contact Information for Business Card

Milo the Pup Strider
Contact: www.milothepupstrider.example
Tel: 07912 358264

```html
<!DOCTYPE html>
<html lang="en">
<head>
<meta charset="utf-8">
<title>Milo the Pup Strider – Business Card</title>
<link rel="stylesheet" href="https://fonts.googleapis.com/css2?family=Questrial&family=Arimo:wght@700&display=swap">
<style>
  :root {
    --lime: #b3e000;
    --ink: #111111;
    --backdrop: #ececec;
    --card-w: 500px;
    --card-h: 286px;
  }
  * { box-sizing: border-box; margin: 0; padding: 0; }
  html, body {
    width: 1200px;
    height: 814px;
    overflow: hidden;
    background: var(--backdrop);
  }
  .sheet {
    width: 1200px;
    height: 814px;
    display: flex;
    align-items: center;
    justify-content: center;
    gap: 60px;
  }
  .card {
    position: relative;
    width: var(--card-w);
    height: var(--card-h);
    overflow: hidden;
    box-shadow: 0 6px 18px rgba(0,0,0,0.12);
  }

  /* Front */
  .card--front { background: var(--lime); }
  .front__band {
    position: absolute;
    left: 0; right: 0;
    top: 150px;
    height: 104px;
    background: var(--ink);
  }
  .brand {
    position: absolute;
    top: 62px;
    left: 0; right: 0;
    display: flex;
    align-items: center;
    justify-content: center;
    gap: 12px;
  }
  .brand__mark {
    width: 22px;
    height: 22px;
    background: var(--ink);
  }
  .brand__name {
    font-family: "Questrial", sans-serif;
    font-size: 34px;
    color: var(--ink);
    letter-spacing: 0.5px;
  }
  .contact {
    position: absolute;
    left: 34px;
    top: 190px;
    font-family: "Questrial", sans-serif;
    font-size: 14px;
    color: var(--lime);
    letter-spacing: 0.3px;
  }
  .contact__sep { padding: 0 6px; }

  /* Back */
  .card--back { background: var(--ink); }
  .back__scene {
    position: absolute;
    left: 120px;
    top: 24px;
    width: 260px;
    height: 110px;
    background: linear-gradient(90deg, #2a3300, #4f6400 50%, #2a3300);
    border-radius: 6px;
  }
  .back__band {
    position: absolute;
    left: 0; right: 0;
    top: 150px;
    bottom: 0;
    background: var(--lime);
  }
  .address {
    position: absolute;
    top: 174px;
    left: 0; right: 0;
    text-align: center;
    font-family: "Arimo", sans-serif;
    font-weight: 700;
    font-size: 13.5px;
    line-height: 1.5;
    color: var(--ink);
  }
</style>
</head>
<body>
  <main class="sheet">
    <section class="card card--front" aria-label="Business card front">
      <div class="front__band"></div>
      <div class="brand">
        <span class="brand__mark"></span>
        <span class="brand__name">Milo the Pup Strider</span>
      </div>
      <p class="contact">Tel: 07912 358264<span class="contact__sep">|</span>www.milothepupstrider.example</p>
    </section>

    <section class="card card--back" aria-label="Business card back">
      <div class="back__scene" role="img" aria-label="Lime silhouette of a walker leading three dogs on leads"></div>
      <div class="back__band"></div>
      <p class="address">12 Orchard Row, Meadow Lane Brookfield,<br>Northam NR4 2QT</p>
    </section>
  </main>
</body>
</html>
```